6x9 Postcard "401k Rollover" to market Individuals to transfer their retirement savings to our firm

Formats: .jpg, .png, .psd, .ai
Dimensions: See uploaded documents

We need a postcard to encourage people 45-65 years olds to transfer their retirement plan assets to our financial advising firm. We have uploaded an example we've been working please feel free to use your artistic license to make it look good images etc. You do not need to copy it word for word, we welcome creativity.

Suggested Wording:

We make it easy to rollover your old 401k

Spread the word! If you or someone you know has a 401k with a former employer or has reached age 59 1/2, consider a 401k rollover

The Pomfret Financial team can help rollover your old 401k

Advantages of a rollover: control over your accounts, more investment options, professional investment management, consolidate and simplify your accounts, guaranteed lifetime income options, help from a team of dedicated advisors

Make the most of your old 401k with a new Rollover IRA, speak with a trusted advisor today, (661)555-0147

If the QRM logo is used it MUST be used with the name "Gerald Pomfret" near it to clearly associate the two. if the words are used they Must be after his name and in all caps like this "Gerald Pomfret, ACCREDITED WEALTH STEWARD TM" [super script TM]. These are rules of the QRM trade mark.

Target Market(s)

Age 45 to 65 with sizable assets in 401k retirement plans

Industry/Entity Type

Investment Advisory

Font styles to use
Serif
Sans Serif
Decorative
Script

Colors

Designer to choose colors to be used in the design.

Requirements
Must have
• The post card MUST contain the following text at least 8pt font:
• Securities offered through Marlowe Ridge Securities, L.P. Member - NEVOA/DTRB | 4870 North Blvd K, Ste 210, Lancaster, CA 93536 | 800.555.0193 | CA Ins. Lic. #0K48391, #0519374, #0K27508, #0746290
• Must have website and phone number:
• www.geraldpomfretwealthco.com
• (661) 555-0147
Nice to have
• We would like the design to convey: Trust, Safety, Growth, Wealth, Planning, Strength, Stable, Peace of Mind, Time, Classic, Legacy

```html
<!DOCTYPE html>
<html lang="en">
<head>
<meta charset="utf-8">
<title>Pomfret Financial – 401k Rollover Postcard</title>
<link rel="stylesheet" href="https://fonts.googleapis.com/css2?family=Montserrat:wght@300;400;700;800&family=Source+Sans+3:wght@400;600;700&display=swap">
<style>
:root{
  --page:#e9e9e9;
  --card:#ffffff;
  --gold:#fdcb33;
  --gold-deep:#e7b024;
  --panel-a:#efbc2c;
  --panel-b:#dfa824;
  --ink:#111111;
  --gray:#6b6b6b;
  --rule:#bdbdbd;
  --white:#ffffff;
}
*{margin:0;padding:0;box-sizing:border-box}
html,body{width:941px;height:1200px;overflow:hidden;background:var(--page)}
body{position:relative;font-family:"Source Sans 3",Arial,sans-serif;color:var(--gray)}

.card{position:absolute;left:102px;width:725px;height:483px;background:var(--card);box-shadow:0 3px 10px rgba(0,0,0,.25);overflow:hidden}
.card--front{top:63px}
.card--back{top:626px}

/* FRONT */
.hero-photo{position:absolute;left:0;top:66px;width:725px;height:362px;
  background:linear-gradient(180deg,#37472d 0%,#4d5b3a 25%,#6d7a5c 45%,#8a9690 62%,#9ea39d 78%,#b9b0a4 100%)}
.hero-photo::after{content:"";position:absolute;inset:0;background:linear-gradient(90deg,rgba(30,35,25,.45) 0%,rgba(30,35,25,.15) 45%,rgba(0,0,0,0) 70%)}
.topbar-rule{position:absolute;left:240px;right:0;top:63px;height:2px;background:var(--rule)}
.tagline{position:absolute;left:252px;top:33px;font-family:"Source Sans 3",sans-serif;font-size:15.5px;color:#8a8a8a;letter-spacing:.1px;white-space:nowrap}
.brand-block{position:absolute;left:0;top:0;width:240px;height:117px;background:var(--gold)}
.brand-tab{position:absolute;left:0;top:0}
.brand-name{position:absolute;left:30px;top:26px;font-family:"Montserrat",sans-serif;font-weight:700;font-size:20px;color:var(--white);letter-spacing:.3px;white-space:nowrap}
.brand-mark{position:absolute;left:30px;top:60px;display:flex;align-items:center;gap:8px;font-family:"Montserrat",sans-serif;font-weight:700;color:var(--white);white-space:nowrap}
.brand-mark__square{width:12px;height:12px;background:var(--white)}
.brand-mark__name{font-size:17px;letter-spacing:1px}
.brand-mark__title{font-size:9.5px;letter-spacing:1.8px;line-height:1.35}
.brand-mark__title sup{font-size:6px}

.headline-rule{position:absolute;left:23px;width:217px;height:1px;background:rgba(255,255,255,.85)}
.headline{position:absolute;left:23px;top:186px;font-family:"Montserrat",sans-serif;font-weight:400;font-size:27px;line-height:44.5px;color:var(--white);text-transform:uppercase;letter-spacing:.3px;white-space:nowrap}
.headline em{font-style:normal;color:var(--gold)}
.subhead{position:absolute;left:23px;top:331px;font-size:16px;color:var(--white)}

.contact-rule{position:absolute;left:0;right:0;top:428px;height:2px;background:#d6d6d6}
.contact{position:absolute;top:446px;display:flex;align-items:center;gap:8px;font-size:11.5px;color:#444;white-space:nowrap}
.contact__icon{width:16px;height:16px;border-radius:3px;background:var(--gold);display:flex;align-items:center;justify-content:center}
.contact--address{left:22px}
.contact--phone{left:343px}
.contact--web{left:514px}

/* BACK */
.about__title{position:absolute;left:22px;top:22px;font-size:14.5px;color:var(--gold-deep)}
.about__text{position:absolute;left:22px;top:46px;width:341px;font-size:10px;line-height:13.4px;color:#555;text-align:justify}
.signature{position:absolute;left:382px;top:22px;font-family:"Montserrat",sans-serif;font-weight:700;color:var(--ink);white-space:nowrap}
.signature__name{font-size:22px;letter-spacing:.2px}
.signature__mark{display:flex;align-items:center;gap:9px;margin-top:10px}
.signature__square{width:14px;height:14px;background:var(--gold)}
.signature__abbr{font-size:19px;letter-spacing:1px}
.signature__title{font-size:10.5px;letter-spacing:2px;line-height:1.45}
.signature__title sup{font-size:6.5px}

.panel-rule{position:absolute;left:0;width:362px;height:2px;background:var(--ink)}
.advantages{position:absolute;left:0;top:142px;width:362px;height:196px;background:linear-gradient(135deg,var(--panel-a) 0%,var(--gold-deep) 55%,var(--panel-b) 100%)}
.advantages__title{position:absolute;left:24px;top:13px;font-size:19.5px;font-weight:600;color:var(--white);letter-spacing:.2px}
.advantages__list{position:absolute;left:33px;top:37px;list-style:none}
.advantages__list li{position:relative;font-size:13.5px;font-weight:600;line-height:23.3px;color:var(--white);padding-left:11px}
.advantages__list li::before{content:"";position:absolute;left:0;top:11px;width:3px;height:3px;border-radius:50%;background:var(--white)}

.cta{position:absolute;left:0;width:362px;top:350px;text-align:center;font-size:10.5px;font-weight:600;line-height:14.5px;color:#222}
.cta-phone{position:absolute;left:0;width:362px;top:388px;display:flex;justify-content:center;align-items:center;gap:7px;font-size:19.5px;font-weight:700;color:var(--ink)}
.disclosure{position:absolute;left:22px;top:420px;font-size:7.4px;line-height:10px;color:#222}
</style>
</head>
<body>

<section class="card card--front">
  <div class="hero-photo" role="img" aria-label="Photo of a retired couple sitting together on a lakeside dock, seen from behind, with a forested shore beyond"></div>

  <div class="topbar-rule"></div>
  <p class="tagline">PERSONALIZED FINANCIAL SERVICES, ESTABLISHED 40 YEARS AGO</p>

  <div class="brand-block">
    <p class="brand-name">GERALD POMFRET</p>
    <div class="brand-mark">
      <span class="brand-mark__square"></span>
      <span class="brand-mark__name">QRM</span>
      <span class="brand-mark__title">ACCREDITED<br>WEALTH<br>STEWARD<sup>TM</sup></span>
    </div>
  </div>
  <svg class="brand-tab" width="280" height="120" aria-hidden="true">
    <polygon points="240,66 274,66 240,117" fill="var(--gold-deep)"/>
  </svg>

  <div class="headline-rule" style="top:180px"></div>
  <h1 class="headline">We make it easy<br>to <em>rollover</em><br>your old <em>401k</em></h1>
  <div class="headline-rule" style="top:321px"></div>
  <p class="subhead">Your choice for Financial Services</p>

  <div class="contact-rule"></div>
  <div class="contact contact--address">
    <span class="contact__icon"><svg width="11" height="10" viewBox="0 0 11 10"><path d="M5.5 0 L11 5 H9.5 V10 H6.5 V7 H4.5 V10 H1.5 V5 H0 Z" fill="#fff"/></svg></span>
    4870 North Blvd K, Ste 210, Lancaster, CA 93536
  </div>
  <div class="contact contact--phone">
    <span class="contact__icon"><svg width="10" height="10" viewBox="0 0 24 24"><path d="M6.6 10.8a15.1 15.1 0 0 0 6.6 6.6l2.2-2.2a1 1 0 0 1 1-.25 11.4 11.4 0 0 0 3.6.57 1 1 0 0 1 1 1V20a1 1 0 0 1-1 1A17 17 0 0 1 3 4a1 1 0 0 1 1-1h3.5a1 1 0 0 1 1 1c0 1.25.2 2.45.57 3.6a1 1 0 0 1-.25 1z" fill="#fff"/></svg></span>
    (661) 555-0147
  </div>
  <div class="contact contact--web">
    <span class="contact__icon"><svg width="11" height="11" viewBox="0 0 12 12" fill="none" stroke="#fff" stroke-width="1"><circle cx="6" cy="6" r="5"/><ellipse cx="6" cy="6" rx="2.2" ry="5"/><line x1="1" y1="6" x2="11" y2="6"/></svg></span>
    www.geraldpomfretwealthco.com
  </div>
</section>

<section class="card card--back">
  <h2 class="about__title">About Us</h2>
  <p class="about__text">Pomfret Financial, Inc., provides investment advice to individuals all over the United States. We specialize in growing and protecting wealth to help people achieve the future they want and provide sustainable retirement income that cannot be out lived. We offer life insurance, long-term care insurance, and inheritance insurance to protect families and provide for the next generations.</p>

  <div class="signature">
    <p class="signature__name">GERALD POMFRET</p>
    <div class="signature__mark">
      <span class="signature__square"></span>
      <span class="signature__abbr">QRM</span>
      <span class="signature__title">ACCREDITED<br>WEALTH<br>STEWARD<sup>TM</sup></span>
    </div>
  </div>

  <div class="panel-rule" style="top:138px"></div>
  <div class="advantages" role="img" aria-label="Gold-toned photo of an investment portfolio document with a pen">
    <h3 class="advantages__title">ADVENTAGE OF ROLLOVER</h3>
    <ul class="advantages__list">
      <li>Control over your accounts</li>
      <li>More investment oprtions</li>
      <li>Professional investment managment</li>
      <li>Consolidate and smplify</li>
      <li>Guaranteed lifetime income options</li>
      <li>Help from a team of dedicated advisors</li>
    </ul>
  </div>
  <div class="panel-rule" style="top:338px"></div>

  <p class="cta">Make the most of your old 401k with a new Rollover IRA,<br>speak with a trusted advisor,&nbsp; call Gerald Pomfret</p>
  <div class="cta-phone">
    <svg width="18" height="18" viewBox="0 0 24 24" aria-hidden="true"><path d="M6.6 10.8a15.1 15.1 0 0 0 6.6 6.6l2.2-2.2a1 1 0 0 1 1-.25 11.4 11.4 0 0 0 3.6.57 1 1 0 0 1 1 1V20a1 1 0 0 1-1 1A17 17 0 0 1 3 4a1 1 0 0 1 1-1h3.5a1 1 0 0 1 1 1c0 1.25.2 2.45.57 3.6a1 1 0 0 1-.25 1z" fill="#111"/></svg>
    (661) 555-0147
  </div>

  <p class="disclosure">Securities offered through Marlowe Ridge Securities,<br>L.P. Member - NEVOA/DTRB<br>4870 North Blvd K, Ste 210, Lancaster, CA 93536 | 800.555.0193<br>CA Ins. Lic. #0K48391, #0519374, #0K27508, #0746290</p>
</section>

</body>
</html>
```